Laboratory marketing Flyer

I want to create a flyer that's reflective of all the services our laboratory offers. please review our services at www.qorvantdiagnostics.com as well as about us for our amenities. focus more on areas of testing other than Toxicology, Covid-19 and Neutralizing anti-body titer. More so on UTI, Gastrointestinal, Wound, Genetics and respiratory. attached is a very old/outdated brochure, I want this in one page, vertical, front and back format.

Target Market(s)

medical facilities

Industry/Entity Type

medical

Font styles to use
Sans Serif

Colors
0054AA
0677BA
7BADD7
CADEEF
E8F1F8

Requirements
Must have
• Answer the phone, quick sample collection, fast turnaround time, large test menu, and Tarn-Ledger-Hub integration

```html
<!DOCTYPE html>
<html lang="en">
<head>
<meta charset="utf-8">
<title>Qorvant Diagnostics – Laboratory Flyer, Front and Back</title>
<link href="https://fonts.googleapis.com/css2?family=Montserrat:wght@400;500;600;700;800&display=swap" rel="stylesheet">
<style>
:root{
  --blue-deep:#0054AA;
  --blue:#0677BA;
  --blue-mid:#7BADD7;
  --blue-pale:#CADEEF;
  --blue-mist:#E8F1F8;
  --ink:#111111;
  --white:#ffffff;
  --backdrop:#d6d8da;
}
*{margin:0;padding:0;box-sizing:border-box}
html,body{width:828px;height:1200px;overflow:hidden;background:var(--backdrop)}
body{font-family:"Montserrat",Arial,sans-serif;color:var(--ink);position:relative}

.page{position:absolute;top:319px;width:680px;height:960px;background:var(--white);overflow:hidden;
  transform:scale(0.585);transform-origin:top left;box-shadow:0 6px 18px rgba(0,0,0,.18)}
.page--front{left:10px}
.page--back{left:420px}
.abs{position:absolute}

/* ---------- FRONT ---------- */
.hero-photo{left:330px;top:0;width:350px;height:358px;
  background:linear-gradient(135deg,#eef5fb 0%,#bcd6ee 40%,#75a7d6 75%,#3573b3 100%);
  clip-path:polygon(12px 0,350px 0,350px 358px,20px 358px,92px 90px)}
.brand{left:0;top:0;width:345px;height:178px;display:flex;align-items:center;justify-content:center;gap:10px}
.brand-dot{width:22px;height:22px;border-radius:50%;background:var(--blue)}
.brand-name{font-weight:700;font-size:27px;color:var(--blue);line-height:1.1}

.hero-band{left:0;top:178px;width:410px;height:180px;background:var(--blue);
  clip-path:polygon(0 0,380px 0,406px 90px,346px 180px,0 180px);color:var(--white);padding:20px 0 0 47px}
.hero-band h1{font-weight:800;font-size:26px;line-height:1.13;text-transform:uppercase}
.hero-band p{font-weight:500;font-size:19px;line-height:1.17;text-transform:uppercase;margin-top:6px}

.promise{left:0;top:378px;width:680px;text-align:center;color:var(--blue);font-size:20px;line-height:1.23;
  text-transform:uppercase;font-weight:600}
.promise strong{font-weight:800}

.perks{left:0;top:467px;width:680px;height:62px;background:var(--blue-mist);text-align:center;color:var(--blue);
  font-weight:600;font-size:13.5px;line-height:1.55;padding-top:9px}
.perks .tick{display:inline-block;width:11px;height:11px;vertical-align:-1px;margin:0 5px}

.about-bar{left:0;top:545px;width:368px;height:32px;background:var(--blue);
  clip-path:polygon(0 0,368px 0,360px 32px,0 32px);color:var(--white);font-weight:600;font-size:15px;padding:7px 0 0 47px}
.about-photo{left:340px;top:545px;width:340px;height:307px;
  background:linear-gradient(160deg,#e2ecf6 0%,#abc8e4 45%,#5b90c5 80%,#2c609a 100%);
  clip-path:polygon(28px 0,340px 0,340px 307px,0 307px)}
.about-text{left:47px;top:598px;width:272px;font-size:10.8px;line-height:1.42}
.about-text p+p{margin-top:11px}

/* ---------- SHARED FOOTER ---------- */
.footer-contact{left:0;top:852px;width:330px;height:108px;background:#000;color:var(--white);
  padding:26px 0 0 47px;font-size:12.5px;font-weight:500;line-height:1.28}
.footer-contact .row{display:flex;gap:8px;align-items:flex-start}
.footer-contact .row+.row{margin-top:9px}
.footer-contact svg{flex:none;margin-top:1px}
.footer-phone{left:300px;top:852px;width:380px;height:108px;background:var(--blue);
  clip-path:polygon(18px 0,380px 0,380px 108px,0 108px);display:flex;align-items:center;justify-content:center;gap:6px;
  color:var(--white);font-weight:700;font-size:36px;padding-left:14px}

/* ---------- BACK ---------- */
.top-rule{left:0;top:0;width:680px;height:14px;background:var(--blue-mid)}
.services-title{left:47px;top:42px;font-size:16.5px;line-height:1.42;font-weight:600;text-transform:uppercase;color:var(--ink)}
.services-title span{display:block;color:var(--blue)}

.service{display:flex;align-items:center;gap:8px;font-size:10.6px;line-height:1.25;color:var(--ink);font-weight:500}
.service .ico{flex:none;width:40px;height:40px;border-radius:50%;background:var(--blue);display:flex;align-items:center;justify-content:center}

.benefit-panel{left:29px;top:280px;width:623px;height:420px;background:var(--blue);
  clip-path:polygon(0 44px,343px 44px,370px 0,623px 0,623px 420px,0 420px)}
.benefits-title{left:390px;top:304px;color:var(--white);font-weight:800;font-size:24px}
.benefit-ico{width:36px;height:36px;border-radius:50%;background:var(--white);display:flex;align-items:center;justify-content:center}
.benefit-head{color:var(--white);font-weight:700;font-size:12.5px;line-height:1.2}
.benefit-head--caps{text-transform:uppercase}
.ticks{list-style:none;color:var(--white);font-size:11.4px;line-height:1.33}
.ticks li{position:relative;padding-left:18px}
.ticks li+li{margin-top:4px}
.ticks--spaced li+li{margin-top:15px}
.ticks li::before{content:"";position:absolute;left:0;top:3px;width:11px;height:11px;border-radius:50%;background:var(--white)}
.ticks li::after{content:"";position:absolute;left:3.5px;top:5.5px;width:4px;height:2.5px;border-left:1.6px solid var(--blue);
  border-bottom:1.6px solid var(--blue);transform:rotate(-45deg)}

.strip{left:0;top:710px;width:680px;height:132px}
.strip-photo{position:absolute;top:0;height:132px}
.strip-photo--a{left:0;width:230px;background:linear-gradient(135deg,#eef2f6,#b9c9db 60%,#6f8fb2);clip-path:polygon(0 0,230px 0,205px 132px,0 132px)}
.strip-photo--b{left:211px;width:270px;background:linear-gradient(135deg,#e5ecf3,#a9bfd6 55%,#56789e);clip-path:polygon(25px 0,270px 0,245px 132px,0 132px)}
.strip-photo--c{left:462px;width:218px;background:linear-gradient(135deg,#6f8fae,#2f4d6e 55%,#142a44);clip-path:polygon(25px 0,218px 0,218px 132px,0 132px)}
</style>
</head>
<body>

<!-- FRONT SIDE -->
<article class="page page--front">
  <div class="abs hero-photo" role="img" aria-label="Lab scientist in cap and mask looking through a microscope"></div>

  <header class="abs brand">
    <span class="brand-dot"></span>
    <span class="brand-name">Qorvant<br>Diagnostics</span>
  </header>

  <section class="abs hero-band">
    <h1>State-of-the-art<br>lab diagnostics</h1>
    <p>Get fast, precise results<br>through the most<br>innovative testing</p>
  </section>

  <h2 class="abs promise">We provide our partners with industry<br><strong>leading less than 30-hour turnaround time</strong><br>for quantitative results.</h2>

  <section class="abs perks">
    Answer the phone<svg class="tick" viewBox="0 0 16 16"><circle cx="8" cy="8" r="8" fill="#0677BA"/><path d="M4.5 8.2l2.3 2.3 4.7-4.8" stroke="#fff" stroke-width="2" fill="none"/></svg>quick sample collection<svg class="tick" viewBox="0 0 16 16"><circle cx="8" cy="8" r="8" fill="#0677BA"/><path d="M4.5 8.2l2.3 2.3 4.7-4.8" stroke="#fff" stroke-width="2" fill="none"/></svg>fast turnaround time<br>
    large test menu, and Tarn-Ledger-Hub integration
  </section>

  <div class="abs about-bar">ABOUT US</div>
  <div class="abs about-photo" role="img" aria-label="Scientist in protective suit working at a microscope"></div>
  <section class="abs about-text">
    <p>At Qorvant we strive at providing our patients with the best quality care by providing physicians, hospitals, medical centers, clinics, and healthcare facilities with state-of-the-art urine drug confirmation testing for the most commonly scheduled prescription drugs and narcotics.</p>
    <p>The highly complex method developed by our team will most definitely detect, and confirm the presence and concentration of scheduled prescription drugs and illicit narcotics which will aid your practice in providing a lab-guided medication management program for your patients.</p>
  </section>

  <footer>
    <div class="abs footer-contact">
      <div class="row"><svg width="10" height="14" viewBox="0 0 12 16"><path d="M6 0a6 6 0 0 0-6 6c0 4.5 6 10 6 10s6-5.5 6-10a6 6 0 0 0-6-6zm0 8.5A2.5 2.5 0 1 1 6 3.5a2.5 2.5 0 0 1 0 5z" fill="#7BADD7"/></svg><span>4120 Alder Ridge Pkwy,<br>Suite 210 Fairhaven, MI 48990</span></div>
      <div class="row"><svg width="11" height="11" viewBox="0 0 14 14"><circle cx="7" cy="7" r="7" fill="#7BADD7"/><path d="M1 7h12M7 1c-2.5 3-2.5 9 0 12M7 1c2.5 3 2.5 9 0 12" fill="none" stroke="#000" stroke-width="1"/></svg><span>www.qorvantdiagnostics.com</span></div>
    </div>
    <div class="abs footer-phone">
      <svg width="22" height="30" viewBox="0 0 24 30"><path d="M7 1l4 6-3 3c1 4 4 9 8 11l3-3 5 4-3 6C11 27 1 14 3 3z" fill="#fff"/></svg>
      <span>(555) 014-2738</span>
    </div>
  </footer>
</article>

<!-- BACK SIDE -->
<article class="page page--back">
  <div class="abs top-rule"></div>
  <h2 class="abs services-title">Accurate, fast laboratory diagnostic services<span>For medical providers</span></h2>

  <!-- column 1 -->
  <div class="abs service" style="left:47px;top:113px"><span class="ico"><svg width="20" height="20" viewBox="0 0 20 20"><rect x="4" y="2" width="5" height="15" rx="2.5" fill="#fff"/><rect x="11" y="2" width="5" height="15" rx="2.5" fill="#fff"/></svg></span>Blood Testing</div>
  <div class="abs service" style="left:47px;top:162px"><span class="ico"><svg width="20" height="20" viewBox="0 0 20 20"><circle cx="10" cy="10" r="6" fill="#fff"/><circle cx="10" cy="10" r="2" fill="#0677BA"/></svg></span>COVID-19<br>Testing</div>
  <div class="abs service" style="left:47px;top:211px"><span class="ico"><svg width="20" height="20" viewBox="0 0 20 20"><path d="M9 3v7c-2-1-6 1-6 6h6zM11 3v7c2-1 6 1 6 6h-6z" fill="#fff"/></svg></span>Respiratory<br>Pathogen Panel<br>(RPP)</div>
  <div class="abs service" style="left:47px;top:258px"><span class="ico"><svg width="20" height="20" viewBox="0 0 20 20"><circle cx="10" cy="8" r="5" fill="none" stroke="#fff" stroke-width="2.4"/><path d="M10 13v5M7 16h6" stroke="#fff" stroke-width="2.4"/></svg></span>Women's<br>Health qPCR</div>

  <!-- column 2 -->
  <div class="abs service" style="left:190px;top:113px"><span class="ico"><svg width="20" height="20" viewBox="0 0 20 20"><rect x="3" y="3" width="6" height="14" rx="3" fill="#fff"/><circle cx="14" cy="13" r="4" fill="#fff"/></svg></span>Toxicology<br>Testing</div>
  <div class="abs service" style="left:190px;top:162px"><span class="ico"><svg width="20" height="20" viewBox="0 0 20 20"><path d="M10 2l7 3v5c0 4-3 7-7 8-4-1-7-4-7-8V5z" fill="#fff"/></svg></span>Neutralizing<br>Antibody Titer</div>
  <div class="abs service" style="left:190px;top:211px"><span class="ico"><svg width="20" height="20" viewBox="0 0 20 20"><rect x="5" y="2" width="10" height="16" rx="1.5" fill="#fff"/><path d="M8 7h4M8 10h4M8 13h4" stroke="#0677BA" stroke-width="1.4"/></svg></span>Urinary Tract<br>Infection qPCR</div>
  <div class="abs service" style="left:190px;top:258px"><span class="ico"><svg width="20" height="20" viewBox="0 0 20 20"><path d="M5 3h10M5 17h10M6 3c0 5 8 9 8 14M14 3c0 5-8 9-8 14" stroke="#fff" stroke-width="2" fill="none"/></svg></span>Genetic Testing</div>

  <!-- column 3 -->
  <div class="abs service" style="left:345px;top:113px"><span class="ico"><svg width="20" height="20" viewBox="0 0 20 20"><circle cx="7" cy="8" r="4" fill="#fff"/><circle cx="14" cy="13" r="3" fill="#fff"/></svg></span>Sexually<br>Transmitted<br>Infections (STI)</div>
  <div class="abs service" style="left:345px;top:162px"><span class="ico"><svg width="20" height="20" viewBox="0 0 20 20"><rect x="2" y="6" width="16" height="8" rx="2" fill="#fff"/><rect x="8" y="7.5" width="4" height="5" fill="#0677BA"/></svg></span>Wound Panel</div>
  <div class="abs service" style="left:345px;top:211px"><span class="ico"><svg width="20" height="20" viewBox="0 0 20 20"><path d="M5 9V5M8 9V3M11 9V3M14 10V6M5 9c0 5 2 8 6 8s4-3 4-7" stroke="#fff" stroke-width="2.2" fill="none" stroke-linecap="round"/></svg></span>Nail Panel</div>

  <!-- column 4 -->
  <div class="abs service" style="left:487px;top:113px"><span class="ico"><svg width="20" height="20" viewBox="0 0 20 20"><circle cx="10" cy="10" r="7" fill="#fff"/><circle cx="8" cy="8" r="1.6" fill="#0677BA"/><circle cx="12.5" cy="12" r="1.6" fill="#0677BA"/></svg></span>Infectious<br>Diseases</div>
  <div class="abs service" style="left:487px;top:162px"><span class="ico"><svg width="20" height="20" viewBox="0 0 20 20"><path d="M9 2v5c-4 0-6 3-5 6s5 3 7 1 4-1 5 2" stroke="#fff" stroke-width="2.4" fill="none" stroke-linecap="round"/></svg></span>Gastrointestinal<br>Panel</div>

  <!-- benefits -->
  <div class="abs benefit-panel"></div>
  <h3 class="abs benefits-title">OUR BENEFITS</h3>

  <div class="abs benefit-ico" style="left:52px;top:348px"><svg width="18" height="18" viewBox="0 0 20 20"><rect x="4" y="2" width="6" height="15" rx="3" fill="#0677BA"/><circle cx="14" cy="14" r="4" fill="#0677BA"/></svg></div>
  <div class="abs benefit-head" style="left:99px;top:348px;width:230px">Precise results through the most innovative technology</div>
  <ul class="abs ticks ticks--spaced" style="left:99px;top:386px;width:230px">
    <li>All of our drug safety monitoring testing will utilize the LC/MS/MS, otherwise known as the “Superior Standard” for analytical quantitation.</li>
    <li>State-of-the-art method along with precise results means you can trust Qorvant to help formulate safety decisions for your patients.</li>
  </ul>

  <div class="abs benefit-ico" style="left:52px;top:534px"><svg width="20" height="20" viewBox="0 0 20 20"><circle cx="10" cy="11" r="6.5" fill="none" stroke="#0677BA" stroke-width="2"/><path d="M10 7v4l3 2M8 2h4" stroke="#0677BA" stroke-width="2" fill="none"/></svg></div>
  <div class="abs benefit-head benefit-head--caps" style="left:99px;top:540px">Prompt results</div>
  <ul class="abs ticks" style="left:99px;top:562px;width:230px">
    <li>We provide our partners with industry leading 48-hour turnaround time for quantitative results.<br>We accomplish this through the optimization of our laboratory testing procedure and by employing the most qualified and experienced laboratory staff.</li>
  </ul>

  <div class="abs benefit-ico" style="left:344px;top:348px"><svg width="18" height="18" viewBox="0 0 20 20"><rect x="4" y="2" width="12" height="16" rx="1.5" fill="#0677BA"/><path d="M7 14v-3M10 14V8M13 14v-5" stroke="#fff" stroke-width="1.6"/></svg></div>
  <div class="abs benefit-head" style="left:390px;top:350px">Comprehensive Customized Panels</div>
  <ul class="abs ticks" style="left:390px;top:372px;width:250px">
    <li>We deliver a widespread customizable offering of urine drug testing panels.</li>
  </ul>

  <div class="abs benefit-ico" style="left:344px;top:428px"><svg width="20" height="20" viewBox="0 0 20 20"><path d="M8 3h4v8H8zM5 17h11M6 14c0 2 8 2 8-3" stroke="#0677BA" stroke-width="2" fill="none"/></svg></div>
  <div class="abs benefit-head" style="left:390px;top:434px">Our Amenities</div>
  <ul class="abs ticks" style="left:390px;top:456px;width:250px">
    <li>Tailored collection and pick-up services</li>
    <li>A widespread drug safety testing menu</li>
    <li>Customizable drug testing possibilities</li>
    <li>Remote consultation with our toxicology experts</li>
    <li>Simple, easy-to-read and time sensible reports</li>
    <li>Numerous reporting options</li>
  </ul>

  <!-- photo strip -->
  <div class="abs strip">
    <div class="strip-photo strip-photo--a" role="img" aria-label="Lab team in white coats reviewing results on a tablet"></div>
    <div class="strip-photo strip-photo--b" role="img" aria-label="Scientists working at benches in a bright laboratory"></div>
    <div class="strip-photo strip-photo--c" role="img" aria-label="Close view of a microscope in a dim lab"></div>
  </div>

  <footer>
    <div class="abs footer-contact">
      <div class="row"><svg width="10" height="14" viewBox="0 0 12 16"><path d="M6 0a6 6 0 0 0-6 6c0 4.5 6 10 6 10s6-5.5 6-10a6 6 0 0 0-6-6zm0 8.5A2.5 2.5 0 1 1 6 3.5a2.5 2.5 0 0 1 0 5z" fill="#7BADD7"/></svg><span>4120 Alder Ridge Pkwy,<br>Suite 210 Fairhaven, MI 48990</span></div>
      <div class="row"><svg width="11" height="11" viewBox="0 0 14 14"><circle cx="7" cy="7" r="7" fill="#7BADD7"/><path d="M1 7h12M7 1c-2.5 3-2.5 9 0 12M7 1c2.5 3 2.5 9 0 12" fill="none" stroke="#000" stroke-width="1"/></svg><span>www.qorvantdiagnostics.com</span></div>
    </div>
    <div class="abs footer-phone">
      <svg width="22" height="30" viewBox="0 0 24 30"><path d="M7 1l4 6-3 3c1 4 4 9 8 11l3-3 5 4-3 6C11 27 1 14 3 3z" fill="#fff"/></svg>
      <span>(555) 014-2738</span>
    </div>
  </footer>
</article>

</body>
</html>
```